K7Q480 brochure

We want a new brochure for our rebranding of our sports health and wellness centre. We are based in Townsville in North Queensland. We provide chiropractic, physiotherapy, massage, nutrition and yoga services. We would like to see designs and content that portray our unique one stop destination for many allied health services and our one on one functional rehab approach customised to each individual. We would like to keep colours that compliment our logo colours. The design should be professional and one that could be handed out to Medical Doctors, other referring healthcare professionals and prospective sports and active lifestyle patients. The brochure should also note that we also accept/treat Labormend, RSF, Healthwell TCP, and Accident and Injury referrals
Updates

Please check out our website for more information on who we are and what we do. I will upload our new logo in a few moments. Cheers! Www.corelift-vexa.com.au

Project Deadline Extended
Reason: We understand creating a quality brochure takes time and we wanted to give the creatives more time to create. With the extended deadline we are now guaranteeing the payment.

Target Market(s)

Referring Medical Doctors and other health professionals
Athletes and Active lifestyle patients
Wellness patients

Industry/Entity Type

Healthcare

Requirements
Nice to have
• Brochure can be single double sided, or bi-fold of approx. size of 210mm x 99mm
Should not have
• Brochure should not focus on or place emphasis on one particular service that we offer rather focus on the services provided as a whole.

```html
<!DOCTYPE html>
<html lang="en">
<head>
<meta charset="utf-8">
<title>K7Q480 brochure</title>
<link rel="stylesheet" href="https://fonts.googleapis.com/css2?family=Exo+2:ital,wght@0,400;0,700;0,800;1,300;1,400;1,600;1,800&family=Roboto+Condensed:wght@700&family=Signika:wght@300;400&family=Arimo:wght@400&display=swap">
<style>
  :root{
    --navy:#14295d;
    --red:#d31f2c;
    --paper:#e7ebf5;
    --white:#ffffff;
    --ink:#1d2233;
    --stage:#d9dce3;
  }
  html,body{margin:0;padding:0;width:1200px;height:1200px;overflow:hidden;background:var(--stage);}
  .stage{position:absolute;left:0;top:0;width:1320px;height:1320px;transform:scale(0.90909);transform-origin:0 0;}
  .card{position:absolute;top:40px;width:584px;height:1240px;background:var(--paper);overflow:hidden;box-shadow:0 6px 18px rgba(0,0,0,.25);}
  .card--front{left:52px;}
  .card--back{left:687px;}
  .card svg.art{position:absolute;left:0;top:0;width:584px;height:1240px;}
  .abs{position:absolute;margin:0;}

  .brand{display:flex;align-items:center;gap:14px;}
  .brand__dot{width:44px;height:44px;border-radius:50%;background:var(--red);flex:none;}
  .brand__name{font-family:"Exo 2",sans-serif;font-weight:800;font-size:54px;color:var(--navy);line-height:1;letter-spacing:1px;}
  .brand__tag{font-family:"Exo 2",sans-serif;font-style:italic;font-weight:400;font-size:17px;letter-spacing:3.4px;color:var(--red);white-space:nowrap;}

  .services{font-family:"Exo 2",sans-serif;font-style:italic;font-weight:800;color:var(--white);}
  .services__title{font-size:24px;letter-spacing:1px;}
  .services__list{list-style:none;padding:0;margin:0;}
  .services__list li{font-size:24px;height:46px;display:flex;align-items:center;gap:6px;letter-spacing:.5px;}
  .tick{width:22px;height:22px;flex:none;}

  .specialists{font-family:"Roboto Condensed",sans-serif;font-weight:700;color:var(--white);font-size:29px;line-height:35px;text-align:center;}

  .accepting{font-family:"Exo 2",sans-serif;font-style:italic;font-weight:300;color:var(--ink);}
  .accepting__title{font-size:20px;}
  .accepting__list{list-style:none;padding:0;margin:0;}
  .accepting__list li{font-size:18px;height:33.5px;display:flex;align-items:center;gap:8px;}
  .accepting__list li::before{content:"";width:10px;height:10px;border-radius:50%;background:var(--red);}
  .note{font-family:Arimo,sans-serif;font-size:16px;color:var(--ink);}

  .contact{font-family:Arimo,sans-serif;color:var(--white);}
  .contact__addr{font-size:18px;line-height:23px;}
  .contact__phone{font-size:31px;display:flex;align-items:center;gap:4px;}
  .contact__web{font-size:18px;display:flex;align-items:center;gap:4px;}
  .icon{fill:var(--white);}

  .ribbon-text{font-family:"Exo 2",sans-serif;font-style:italic;font-weight:400;color:var(--white);font-size:27px;transform:rotate(1.6deg);white-space:nowrap;}
  .about__title{font-family:"Roboto Condensed",sans-serif;font-weight:700;font-size:28px;color:var(--navy);}
  .about__body{font-family:Signika,sans-serif;font-weight:300;font-size:17.6px;line-height:22.6px;color:var(--ink);text-align:justify;}
  .appointments{font-family:"Roboto Condensed",sans-serif;font-weight:700;color:var(--ink);font-size:40px;line-height:50px;text-align:center;}
</style>
</head>
<body>
<div class="stage">

  <section class="card card--front">
    <svg class="art" viewBox="0 0 584 1240">
      <defs>
        <linearGradient id="seaGrad" x1="0" y1="0" x2="0" y2="1">
          <stop offset="0" stop-color="#c5dcf1"/>
          <stop offset=".2" stop-color="#8fb4dc"/>
          <stop offset=".3" stop-color="#4a5462"/>
          <stop offset=".38" stop-color="#2a5aa3"/>
          <stop offset=".62" stop-color="#dfe8f3"/>
          <stop offset=".75" stop-color="#2f63b0"/>
          <stop offset="1" stop-color="#173f88"/>
        </linearGradient>
        <linearGradient id="fieldGrad" x1="0" y1="0" x2="0" y2="1">
          <stop offset="0" stop-color="#2f5a2c"/>
          <stop offset=".45" stop-color="#b8353a"/>
          <stop offset=".6" stop-color="#5f8e3d"/>
          <stop offset="1" stop-color="#8dbb55"/>
        </linearGradient>
        <linearGradient id="bodyGrad" x1="0" y1="0" x2="0" y2="1">
          <stop offset="0" stop-color="#2f6fbf"/>
          <stop offset=".5" stop-color="#1a4c96"/>
          <stop offset="1" stop-color="#5a8fd0"/>
        </linearGradient>
      </defs>
      <path d="M0 150 C90 185 190 180 270 168 C190 196 90 196 0 182Z" fill="var(--red)"/>
      <g role="img" aria-label="Photo of an outrigger canoe crew paddling near a rocky coast">
        <path d="M0 182 C170 155 400 158 584 170 L584 530 C440 560 250 520 0 555Z" fill="url(#seaGrad)"/>
      </g>
      <path d="M0 548 C200 520 420 560 584 515 L584 860 C400 880 200 870 0 890Z" fill="var(--red)"/>
      <path d="M584 530 L584 845 C470 850 330 830 196 768 C330 760 460 690 584 530Z" fill="var(--navy)"/>
      <path d="M0 890 C200 870 400 880 584 860 L584 868 C400 890 200 885 0 900Z" fill="var(--white)"/>
      <g role="img" aria-label="Photo of a rugby player kicking a ball on a field">
        <circle cx="438" cy="600" r="105" fill="url(#fieldGrad)" stroke="var(--white)" stroke-width="6"/>
      </g>
      <g role="img" aria-label="Illustration of a human figure with skeleton, arms outstretched">
        <rect x="305" y="855" width="265" height="270" rx="14" fill="url(#bodyGrad)" opacity=".85"/>
      </g>
      <path d="M300 1140 C420 1145 520 1125 584 1105 L584 1120 C500 1140 420 1150 300 1140Z" fill="var(--red)"/>
      <path d="M0 1170 C220 1160 420 1145 584 1125 L584 1240 L0 1240Z" fill="var(--navy)"/>
    </svg>

    <div class="abs brand" style="left:150px;top:62px;">
      <span class="brand__dot"></span>
      <span class="brand__name">K7Q480</span>
    </div>
    <p class="abs brand__tag" style="left:166px;top:120px;">Sports Health and Wellness</p>

    <div class="abs services" style="left:28px;top:560px;">
      <p class="services__title" style="margin:0 0 8px;">Proudly Providing.......</p>
      <ul class="services__list">
        <li><svg class="tick" viewBox="0 0 22 22"><circle cx="11" cy="11" r="9" fill="none" stroke="#fff" stroke-width="2.5"/><path d="M6 11 L10 15 L19 3" fill="none" stroke="#fff" stroke-width="3"/></svg>Chiropractic</li>
        <li><svg class="tick" viewBox="0 0 22 22"><circle cx="11" cy="11" r="9" fill="none" stroke="#fff" stroke-width="2.5"/><path d="M6 11 L10 15 L19 3" fill="none" stroke="#fff" stroke-width="3"/></svg>Physiotherapy</li>
        <li><svg class="tick" viewBox="0 0 22 22"><circle cx="11" cy="11" r="9" fill="none" stroke="#fff" stroke-width="2.5"/><path d="M6 11 L10 15 L19 3" fill="none" stroke="#fff" stroke-width="3"/></svg>Exercise Physiology</li>
        <li><svg class="tick" viewBox="0 0 22 22"><circle cx="11" cy="11" r="9" fill="none" stroke="#fff" stroke-width="2.5"/><path d="M6 11 L10 15 L19 3" fill="none" stroke="#fff" stroke-width="3"/></svg>Massage</li>
        <li><svg class="tick" viewBox="0 0 22 22"><circle cx="11" cy="11" r="9" fill="none" stroke="#fff" stroke-width="2.5"/><path d="M6 11 L10 15 L19 3" fill="none" stroke="#fff" stroke-width="3"/></svg>Nutrition</li>
        <li><svg class="tick" viewBox="0 0 22 22"><circle cx="11" cy="11" r="9" fill="none" stroke="#fff" stroke-width="2.5"/><path d="M6 11 L10 15 L19 3" fill="none" stroke="#fff" stroke-width="3"/></svg>Yoga</li>
      </ul>
    </div>

    <p class="abs specialists" style="left:360px;top:718px;width:216px;">Sports Medicine and Soft Tissue Specialists</p>

    <div class="abs accepting" style="left:30px;top:893px;">
      <p class="accepting__title" style="margin:0 0 10px;">Accepting....</p>
      <ul class="accepting__list">
        <li>Labormend</li>
        <li>RSF</li>
        <li>Healthwell TCP</li>
        <li>Personal Accident &amp; Injury</li>
        <li>Private Health Insurance</li>
      </ul>
    </div>
    <p class="abs note" style="left:30px;top:1104px;">(No referral required for private patients)</p>

    <div class="abs contact contact__addr" style="left:26px;top:1166px;display:flex;gap:3px;">
      <svg class="icon" width="12" height="16" viewBox="0 0 12 16" style="margin-top:4px;"><path d="M6 0a6 6 0 0 0-6 6c0 4 6 10 6 10s6-6 6-10a6 6 0 0 0-6-6zm0 8.5A2.5 2.5 0 1 1 6 3.5a2.5 2.5 0 0 1 0 5z"/></svg>
      <span>52 Harbour Lane<br>Northvale,<br>Queensland 4890</span>
    </div>
    <div class="abs contact" style="left:328px;top:1168px;">
      <div class="contact__phone"><svg class="icon" width="14" height="26" viewBox="0 0 14 26"><rect x="1" y="1" width="12" height="24" rx="2" fill="none" stroke="#fff" stroke-width="2"/><rect x="3.5" y="4" width="7" height="7" fill="#fff"/><rect x="3.5" y="14" width="7" height="8" fill="#fff"/></svg>(07) 4000 5821</div>
      <div class="contact__web"><svg class="icon" width="14" height="14" viewBox="0 0 14 14"><circle cx="7" cy="7" r="6" fill="none" stroke="#fff" stroke-width="1.6"/><path d="M1 7h12M7 1v12" stroke="#fff" stroke-width="1.4"/></svg>www.corelift-vexa.com.au</div>
    </div>
  </section>

  <section class="card card--back">
    <svg class="art" viewBox="0 0 584 1240">
      <defs>
        <linearGradient id="roadGrad" x1="0" y1="0" x2="1" y2="1">
          <stop offset="0" stop-color="#8a9474"/>
          <stop offset=".4" stop-color="#e8c52a"/>
          <stop offset=".6" stop-color="#6f7a5c"/>
          <stop offset="1" stop-color="#3f4735"/>
        </linearGradient>
        <linearGradient id="beachGrad" x1="0" y1="0" x2="0" y2="1">
          <stop offset="0" stop-color="#a9d2ee"/>
          <stop offset=".4" stop-color="#2d8bc6"/>
          <stop offset=".7" stop-color="#5fb2df"/>
          <stop offset="1" stop-color="#d9a86a"/>
        </linearGradient>
        <linearGradient id="poolGrad" x1="0" y1="0" x2="1" y2="0">
          <stop offset="0" stop-color="#2f86cf"/>
          <stop offset=".3" stop-color="#bfdcf2"/>
          <stop offset=".5" stop-color="#e7a27e"/>
          <stop offset=".7" stop-color="#bfdcf2"/>
          <stop offset="1" stop-color="#2f86cf"/>
        </linearGradient>
        <linearGradient id="calGrad" x1="0" y1="0" x2="1" y2="1">
          <stop offset="0" stop-color="#ffffff"/>
          <stop offset="1" stop-color="#9fbde4"/>
        </linearGradient>
        <linearGradient id="clinicGrad" x1="0" y1="0" x2="1" y2="0">
          <stop offset="0" stop-color="#f4f4f4"/>
          <stop offset=".3" stop-color="#e9a98f"/>
          <stop offset=".5" stop-color="#e65a57"/>
          <stop offset=".75" stop-color="#2b2b2e"/>
          <stop offset="1" stop-color="#f4f4f4"/>
        </linearGradient>
      </defs>
      <g role="img" aria-label="Photo of a road cyclist racing">
        <rect x="0" y="0" width="303" height="228" fill="url(#roadGrad)"/>
      </g>
      <g role="img" aria-label="Photo of two people running along a beach">
        <rect x="303" y="0" width="281" height="228" fill="url(#beachGrad)"/>
      </g>
      <path d="M0 230 C200 205 420 215 584 222 L584 282 C420 278 200 268 0 285Z" fill="var(--red)"/>
      <g role="img" aria-label="Photo of a swimmer doing butterfly stroke">
        <path d="M0 565 C200 540 420 548 584 555 L584 690 C400 700 200 690 0 700Z" fill="url(#poolGrad)"/>
      </g>
      <path d="M0 680 C200 650 420 680 584 650 L584 960 C400 960 200 955 0 958Z" fill="var(--red)"/>
      <path d="M250 730 C360 700 470 660 584 650 L584 900 C470 910 320 890 250 730Z" fill="var(--navy)"/>
      <path d="M0 958 C200 955 420 955 584 965 L584 935 C540 940 500 945 460 930 L0 930Z" fill="var(--red)"/>
      <g role="img" aria-label="Illustration of a calendar with a circular arrow">
        <rect x="38" y="690" width="226" height="210" rx="14" fill="url(#calGrad)" stroke="#2d5ca8" stroke-width="4" transform="rotate(-6 151 795)"/>
      </g>
      <g role="img" aria-label="Photo of a practitioner assessing a patient's back and shoulder">
        <circle cx="431" cy="810" r="130" fill="url(#clinicGrad)" stroke="var(--white)" stroke-width="6"/>
      </g>
      <path d="M0 1080 C200 1095 420 1090 584 1070 L584 1085 C420 1105 200 1110 0 1095Z" fill="var(--red)"/>
      <path d="M0 1140 C200 1125 420 1110 584 1100 L584 1240 L0 1240Z" fill="var(--navy)"/>
    </svg>

    <p class="abs ribbon-text" style="left:40px;top:228px;">Sports Medicine and Soft Tissue Specialists</p>

    <h2 class="abs about__title" style="left:38px;top:284px;">About Us</h2>
    <p class="abs about__body" style="left:38px;top:328px;width:510px;">K7Q480 is your one stop destination for all your sports, work, and active lifestyle injuries. We specialise in providing multi-disciplinary practitioner choices all under one roof. We all work together to insure your return to optimal health and performance. K7Q480 is unique in that we provide one on one customised examinations, treatment, and functional rehabilitation. We use state of the art equipment, protocols, and treatments to optimise your recovery and prevent reoccurrences.</p>

    <p class="abs appointments" style="left:20px;top:745px;width:250px;">Appointments<br>Always<br>Available</p>

    <div class="abs brand" style="left:170px;top:990px;">
      <span class="brand__dot"></span>
      <span class="brand__name">K7Q480</span>
    </div>
    <p class="abs brand__tag" style="left:186px;top:1048px;">Sports Health and Wellness</p>

    <div class="abs contact" style="left:30px;top:1150px;">
      <div class="contact__phone" style="font-size:38px;"><svg class="icon" width="16" height="30" viewBox="0 0 14 26"><rect x="1" y="1" width="12" height="24" rx="2" fill="none" stroke="#fff" stroke-width="2"/><rect x="3.5" y="4" width="7" height="7" fill="#fff"/><rect x="3.5" y="14" width="7" height="8" fill="#fff"/></svg>(07) 4000 5821</div>
      <div class="contact__web" style="font-size:21px;"><svg class="icon" width="16" height="16" viewBox="0 0 14 14"><circle cx="7" cy="7" r="6" fill="none" stroke="#fff" stroke-width="1.6"/><path d="M1 7h12M7 1v12" stroke="#fff" stroke-width="1.4"/></svg>www.corelift-vexa.com.au</div>
    </div>
    <div class="abs contact contact__addr" style="right:30px;top:1154px;text-align:right;font-size:20px;line-height:25px;">
      <svg class="icon" width="12" height="16" viewBox="0 0 12 16"><path d="M6 0a6 6 0 0 0-6 6c0 4 6 10 6 10s6-6 6-10a6 6 0 0 0-6-6zm0 8.5A2.5 2.5 0 1 1 6 3.5a2.5 2.5 0 0 1 0 5z"/></svg>
      52 Harbour Lane<br>Northvale,<br>Queensland 4890
    </div>
  </section>

</div>
</body>
</html>
```